Commercial janitorial company looking for a fresh and modern website design

We need a new website design for our Edmonton, Alberta-based commercial cleaning company called Brevick Custodial Limited. We have been providing services throughout Alberta for over 50 years, and have a strong customer-oriented service reputation. We are working to re-brand our image and the next crucial piece of that is an informative, simple, and modern website. We provide full service office and industrial cleaning, periodic services, and basic building maintenance, with a focus on being a 'silent partner' for our clients, allowing them to focus on their core business services. We are committed to the highest safety standards and industry best practices for productivity, employing environmentally friendly products practices in all our locations.

We would like a visually pleasing, easy-to-navigate website structure that provides clear communication through imagery and minimal text.

Target Market(s)

Commercial businesses

Industry/Entity Type

It Company

Font styles to use
Other font styles liked:
• Segoe (similar to our logo's font)

Requirements
Must have
• We would like the landing page to be extremely straightforward, with minimal scrolling required, and minimal text presence. We will likely have up to 5 sub-menus / pages, leading off from the main landing page. These pages will have further text on them, supplying further information. We would prefer their location on the top of the screen to be locked or in some way present during any page scrolling.
• Our logos are also available in eps, pdf, ai formats.
Nice to have
• Some websites that we like the presentation of include:
• tanglorn.hr
• quintbrook.com
• vox.com
• morvill.com
• tryplanko.com
• zunor.com

```html
<!DOCTYPE html>
<html lang="en">
<head>
<meta charset="utf-8">
<title>Brevick Custodial Limited</title>
<link href="https://fonts.googleapis.com/css2?family=Open+Sans:wght@300;400;600;700&display=swap" rel="stylesheet">
<style>
:root{
  --blue:#1d8fd1;
  --blue-dark:#0f6ea8;
  --green:#6cb33f;
  --ink:#333;
  --muted:#7d7d7d;
  --light:#f2f2f2;
  --footer:#1b1d22;
  --white:#fff;
}
*{box-sizing:border-box;margin:0;padding:0}
html,body{width:745px;height:1200px;overflow:hidden}
body{font-family:"Open Sans",sans-serif;color:var(--ink);background:var(--white);position:relative}
.site-header{position:absolute;top:0;left:0;width:745px;height:38px;background:var(--white);display:flex;align-items:center;padding:0 50px 0 58px;justify-content:space-between;z-index:3;box-shadow:0 1px 2px rgba(0,0,0,.06)}
.brand{display:flex;align-items:center;gap:6px}
.brand-mark{width:14px;height:14px;border-radius:50%;background:var(--blue)}
.brand-name{font-size:14px;font-weight:600;color:var(--blue);letter-spacing:1px}
.main-nav{display:flex;gap:14px;align-items:center}
.main-nav a{font-size:6px;font-weight:600;color:#666;text-decoration:none;letter-spacing:.3px;padding:6px 0;border-bottom:2px solid transparent}
.main-nav a.active{color:var(--blue);border-color:var(--blue)}
.search-icon{width:9px;height:9px}
.hero{position:absolute;top:38px;left:0;width:745px;height:332px}
.hero-photo{position:absolute;inset:0;background:
  linear-gradient(90deg,rgba(40,90,120,.0) 0%,rgba(60,110,130,.35) 30%,rgba(150,80,60,.45) 60%,rgba(140,70,55,.4) 90%),
  linear-gradient(180deg,#6fa6d8 0%,#a9c8e6 22%,#6f93a6 40%,#5d7d8a 60%,#7b5f52 78%,#4d5a3c 92%,#3e4a30 100%)}
.hero-caption{position:absolute;left:58px;top:78px;font-size:17px;font-weight:400;color:var(--white);line-height:1.3;text-shadow:0 1px 4px rgba(0,0,0,.5)}
.hero-arrow{position:absolute;top:160px;width:10px;height:16px}
.hero-curve{position:absolute;bottom:-1px;left:0}
.section-title{display:flex;justify-content:center;align-items:center;gap:8px;font-size:17px;font-weight:400;color:var(--blue)}
.section-title::before,.section-title::after{content:"~";color:var(--blue);font-size:15px}
.welcome{position:absolute;top:412px;left:0;width:745px;text-align:center}
.welcome p{width:580px;margin:16px auto 0;font-size:7px;line-height:1.9;color:var(--muted)}
.operate{position:absolute;top:515px;left:0;width:745px;height:235px}
.operate-bg{position:absolute;inset:0}
.operate-copy{position:absolute;left:58px;top:36px;width:320px;color:var(--white)}
.operate-copy .section-title{justify-content:flex-start;color:var(--white);font-size:16px}
.operate-copy .section-title::before,.operate-copy .section-title::after{color:var(--white)}
.operate-copy p{font-size:6.5px;margin-top:10px}
.facility-list{list-style:none;columns:2;column-gap:20px;margin-top:10px;width:230px}
.facility-list li{font-size:6.5px;line-height:2.1;padding-left:9px;position:relative}
.facility-list li::before{content:"›";position:absolute;left:0}
.btn-dark{display:inline-block;margin-top:16px;background:#2d3a26;color:var(--white);font-size:6.5px;font-weight:700;padding:8px 13px;text-decoration:none}
.operate-media{position:absolute;left:400px;top:30px;width:318px;height:178px;background:linear-gradient(110deg,#b9bfc6 0%,#8e99a6 35%,#5b6b7e 55%,#2f6db5 75%,#1f5aa3 100%)}
.play{position:absolute;left:144px;top:74px;width:30px;height:30px}
.services{position:absolute;top:770px;left:0;width:745px}
.service-grid{display:flex;gap:14px;margin:22px 0 0 58px}
.service-card{width:131px;background:var(--light);text-align:center;padding-bottom:14px}
.service-photo{height:105px}
.service-card h3{font-size:9.5px;font-weight:600;color:var(--blue);margin:12px 0 6px}
.service-card p{font-size:6px;line-height:1.65;color:var(--muted);padding:0 14px}
.read-more{display:inline-block;margin-top:8px;font-size:5.5px;font-weight:700;color:var(--blue-dark);text-decoration:none}
.site-footer{position:absolute;top:1040px;left:0;width:745px;height:160px}
.footer-bg{position:absolute;inset:0}
.copyright{position:absolute;left:58px;top:118px;font-size:5.5px;color:#aaa}
.location{position:absolute;left:330px;top:62px;font-size:5.5px;line-height:1.8;color:#bbb}
.location strong{color:var(--white);font-size:6px}
.map{position:absolute;left:490px;top:66px;width:130px;height:56px;background:linear-gradient(135deg,#ece8de,#d8e1d0 60%,#c9d6e2)}
.to-top{position:absolute;right:40px;top:140px;width:12px;height:12px;background:#333}
</style>
</head>
<body>
<header class="site-header">
  <div class="brand"><span class="brand-mark"></span><span class="brand-name">BREVICK</span></div>
  <nav class="main-nav">
    <a class="active" href="#">HOME</a>
    <a href="#">WHAT WE DO</a>
    <a href="#">WHERE WE OPERATE</a>
    <a href="#">WHO WE ARE</a>
    <a href="#">WORK WITH US</a>
    <a href="#">CONTACT US</a>
    <svg class="search-icon" viewBox="0 0 10 10"><circle cx="4" cy="4" r="3" fill="none" stroke="#666" stroke-width="1.2"/><line x1="6.2" y1="6.2" x2="9" y2="9" stroke="#666" stroke-width="1.2"/></svg>
  </nav>
</header>

<section class="hero">
  <div class="hero-photo" role="img" aria-label="Modern glass and brick office building under a blue sky"></div>
  <p class="hero-caption">Sed ut perspiciatis unde omnis iste natus<br>error sit doloremque laudantium.</p>
  <svg class="hero-arrow" style="left:12px" viewBox="0 0 10 16"><polyline points="8,2 2,8 8,14" fill="none" stroke="#fff" stroke-width="2"/></svg>
  <svg class="hero-arrow" style="right:12px" viewBox="0 0 10 16"><polyline points="2,2 8,8 2,14" fill="none" stroke="#fff" stroke-width="2"/></svg>
  <svg class="hero-curve" width="745" height="40" viewBox="0 0 745 40"><path d="M0 10 Q372 50 745 10 L745 40 L0 40Z" fill="#fff"/></svg>
</section>

<section class="welcome">
  <h2 class="section-title">Welcome To Brevick</h2>
  <p>Since 1965 Brevick Custodial Limited has been providing commercial cleaning services to clients across Alberta. Our team takes pride in long-standing relationships built on trust, care and steady results. We work quietly in the background so that every client can focus on their core business, backed by safe methods, strong training and environmentally friendly products in every location we serve.</p>
</section>

<section class="operate">
  <svg class="operate-bg" width="745" height="235" viewBox="0 0 745 235"><path d="M0 16 Q372 -8 745 16 L745 235 L0 235Z" fill="#6cb33f"/></svg>
  <div class="operate-copy">
    <h2 class="section-title">Where We Operate</h2>
    <p>Brevick provides services to businesses in all corners of the province, including:</p>
    <ul class="facility-list">
      <li>Office facilities</li>
      <li>Government facilities</li>
      <li>Retail facilities</li>
      <li>Financial facilities</li>
      <li>Warehouse facilities</li>
      <li>Manufacturing facilities</li>
      <li>Healthcare facilities</li>
    </ul>
    <a class="btn-dark" href="#">READ MORE</a>
  </div>
  <div class="operate-media" role="img" aria-label="Video still of a worker mopping a floor beside a blue cleaning cart">
    <svg class="play" viewBox="0 0 30 30"><circle cx="15" cy="15" r="15" fill="#fff"/><polygon points="12,9 21,15 12,21" fill="#333"/></svg>
  </div>
</section>

<section class="services">
  <h2 class="section-title">Our Services</h2>
  <div class="service-grid">
    <article class="service-card">
      <div class="service-photo" role="img" aria-label="Blue industrial floor scrubber machine" style="background:linear-gradient(160deg,#cdd5dc 0%,#5c8fc4 45%,#1f5fa8 75%,#6b7480 100%)"></div>
      <h3>Industrial Cleaning</h3>
      <p>We keep offices and plants spotless with trained crews and safe, proven methods.</p>
      <a class="read-more" href="#">READ MORE »</a>
    </article>
    <article class="service-card">
      <div class="service-photo" role="img" aria-label="Worker in blue uniform servicing equipment" style="background:linear-gradient(160deg,#8fa6bd 0%,#2e5f9a 45%,#1b3f73 75%,#b8c2cc 100%)"></div>
      <h3>Periodic Services</h3>
      <p>Scheduled deep cleans for carpets, windows and floors keep every site at its best.</p>
      <a class="read-more" href="#">READ MORE »</a>
    </article>
    <article class="service-card">
      <div class="service-photo" role="img" aria-label="Cleaning cart with mops and buckets" style="background:linear-gradient(160deg,#eef0f2 0%,#9fbddd 40%,#2b74c2 70%,#5e6b78 100%)"></div>
      <h3>Basic Building</h3>
      <p>Routine building care handled quietly so your staff can focus on their daily work.</p>
      <a class="read-more" href="#">READ MORE »</a>
    </article>
    <article class="service-card">
      <div class="service-photo" role="img" aria-label="Floor polishing machine with a red pad" style="background:linear-gradient(160deg,#c9ced3 0%,#8b8f94 40%,#c0443c 70%,#7a2b27 100%)"></div>
      <h3>Maintenance</h3>
      <p>Light repairs and upkeep tasks done fast, safely and with minimal disruption.</p>
      <a class="read-more" href="#">READ MORE »</a>
    </article>
  </div>
</section>

<footer class="site-footer">
  <svg class="footer-bg" width="745" height="160" viewBox="0 0 745 160">
    <path d="M0 30 Q372 -10 745 30 L745 160 L0 160Z" fill="#1d8fd1"/>
    <path d="M0 42 Q372 2 745 40 L745 160 L0 160Z" fill="#6cb33f"/>
    <path d="M0 52 Q372 14 745 50 L745 160 L0 160Z" fill="#1b1d22"/>
  </svg>
  <p class="copyright">© 2016 Brevick Custodial Limited. All rights reserved.</p>
  <div class="location">
    <strong>LOCATION:</strong><br>
    10 Sample Road NW,<br>
    Edmonton, AB T5J 0A0<br>
    Phone: 780-555-0142<br>
    Email: info@brevick.com
  </div>
  <div class="map" role="img" aria-label="Map showing the office location"></div>
  <div class="to-top"></div>
</footer>
</body>
</html>
```